Pure Palm tree rhum label design

We need a label design for a palm tree rhum named 'Voile Cendré'. We have an original design and we need an enhancement or a new design that reflects the product. It is a liquor. The label should be bilingual (French and English). We have original design that gives an idea and can be used as starting point. The text on the label for the existing design has to show up in the new design. The text is uploaded too as well as the existing design.
Update:
- The design must use Oil Palm Tree and not Palm Tree. Sample Images are attached.
- The neck of the bottle has to have the name of the product: Voile Cendré.
- The word 'Liqueur' goes between the volume (1L) and the percentage of alcohol (43% Vol).
- Back side text is provided: see document
- The following description goes between the English and the french version (front and back):
The word: L'Original
The representation of a palm oil tree
The word: Original.
An image is uploaded for that.
No mandatory Fonts or Color or Bakground.

Font styles to use
Serif
Sans Serif
Script

```html
<!DOCTYPE html>
<html lang="fr">
<head>
<meta charset="utf-8">
<title>Voile Cendré — Liqueur label</title>
<link rel="stylesheet" href="https://fonts.googleapis.com/css2?family=Rye&family=Josefin+Sans:wght@400;600;700&display=swap">
<style>
  :root {
    --coral: #F27A5C;
    --coral-deep: #EE6A4C;
    --cream: #ECE8E0;
    --cream-light: #F4F1EB;
    --ink: #45433F;
    --gold: #A88A4F;
    --white: #FFFFFF;
    --palm: #8FA083;
  }
  html, body {
    margin: 0;
    padding: 0;
    width: 1200px;
    height: 1200px;
    overflow: hidden;
    background: var(--coral);
  }
  .canvas {
    position: relative;
    width: 1200px;
    height: 1200px;
    background: var(--coral);
  }
  .neck-label {
    position: absolute;
    left: 386px;
    top: 50px;
    width: 427px;
    height: 179px;
  }
  .front-label {
    position: absolute;
    left: 332px;
    top: 402px;
    width: 535px;
    height: 729px;
  }
  .label-body { fill: var(--cream); }
  .label-frame { fill: none; stroke: var(--coral); stroke-width: 4; }
  .brand-name {
    font-family: "Rye", serif;
    fill: var(--ink);
    stroke: var(--white);
    stroke-width: 5;
    paint-order: stroke;
  }
  .category {
    font-family: "Josefin Sans", sans-serif;
    font-weight: 600;
    fill: var(--coral);
    letter-spacing: 14px;
  }
  .swoosh { fill: none; stroke: var(--coral); stroke-width: 3; stroke-linecap: round; }
  .rule { stroke: var(--coral); stroke-width: 3; }
  .knob { fill: var(--coral); }
  .tagline-band { fill: var(--white); }
  .tagline {
    font-family: "Josefin Sans", sans-serif;
    font-weight: 600;
    font-size: 28px;
    letter-spacing: 5px;
    fill: var(--gold);
  }
  .seal-ring { fill: var(--white); }
  .seal { fill: var(--coral); stroke: var(--gold); stroke-width: 3; }
  .facts-band { fill: var(--coral); }
  .facts {
    font-family: "Josefin Sans", sans-serif;
    font-weight: 700;
    font-size: 40px;
    fill: var(--white);
  }
</style>
</head>
<body>
<main class="canvas">

  <!-- Neck label -->
  <svg class="neck-label" viewBox="0 0 628 263" xmlns="http://www.w3.org/2000/svg">
    <path class="label-body" d="M25,0 H603 Q628,0 628,25 V175 Q628,200 603,200 H540 C500,200 480,263 314,263 C148,263 128,200 88,200 H25 Q0,200 0,175 V25 Q0,0 25,0Z"/>
    <path class="label-frame" d="M35,15 H593 Q613,15 613,35 V165 Q613,185 593,185 H535 C495,185 475,248 314,248 C153,248 133,185 93,185 H35 Q15,185 15,165 V35 Q15,15 35,15Z"/>
    <text class="brand-name" x="314" y="110" font-size="78" text-anchor="middle" textLength="505" lengthAdjust="spacingAndGlyphs">Voile Cendré</text>
    <path class="swoosh" d="M200,132 Q314,150 428,128"/>
    <defs><path id="neck-arc" d="M190,158 Q314,200 438,158"/></defs>
    <text class="category" font-size="30"><textPath href="#neck-arc" startOffset="50%" text-anchor="middle">LIQUEUR</textPath></text>
    <path class="swoosh" d="M175,178 Q314,210 453,172"/>
    <ellipse class="knob" cx="175" cy="178" rx="9" ry="7"/>
    <ellipse class="knob" cx="455" cy="171" rx="9" ry="7"/>
    <circle class="knob" cx="314" cy="218" r="6"/>
  </svg>

  <!-- Front label -->
  <svg class="front-label" viewBox="0 0 787 1072" xmlns="http://www.w3.org/2000/svg">
    <defs>
      <radialGradient id="palm-tone" cx="50%" cy="45%" r="55%">
        <stop offset="0%" stop-color="#A6B49A"/>
        <stop offset="60%" stop-color="#C7CEBC"/>
        <stop offset="100%" stop-color="#ECE8E0" stop-opacity="0"/>
      </radialGradient>
      <path id="front-arc" d="M240,665 Q393,720 546,665"/>
    </defs>
    <path class="label-body" d="M30,80 H140 C180,80 200,0 393,0 C586,0 606,80 646,80 H757 Q787,80 787,110 V1042 Q787,1072 757,1072 H30 Q0,1072 0,1042 V110 Q0,80 30,80Z"/>
    <path class="label-frame" d="M40,98 H150 C190,98 210,20 393,20 C576,20 596,98 636,98 H747 Q769,98 769,120 V1032 Q769,1054 747,1054 H40 Q18,1054 18,1032 V120 Q18,98 40,98Z"/>

    <ellipse role="img" aria-label="Oil palm fronds illustration" cx="395" cy="300" rx="290" ry="200" fill="url(#palm-tone)"/>

    <text class="brand-name" x="393" y="560" font-size="100" text-anchor="middle" textLength="630" lengthAdjust="spacingAndGlyphs">Voile Cendré</text>

    <path class="swoosh" d="M255,625 Q393,650 555,622"/>
    <text class="category" font-size="38"><textPath href="#front-arc" startOffset="50%" text-anchor="middle">LIQUEUR</textPath></text>
    <path class="swoosh" d="M190,685 Q393,735 600,680"/>
    <ellipse class="knob" cx="188" cy="684" rx="12" ry="9"/>
    <ellipse class="knob" cx="602" cy="679" rx="12" ry="9"/>

    <g class="divider">
      <line class="rule" x1="85" y1="725" x2="705" y2="725"/>
      <ellipse class="knob" cx="82" cy="725" rx="8" ry="6"/>
      <ellipse class="knob" cx="708" cy="725" rx="8" ry="6"/>
      <circle class="knob" cx="395" cy="725" r="5"/>
    </g>

    <rect class="tagline-band" x="78" y="763" width="634" height="74"/>
    <text class="tagline" x="195" y="810" text-anchor="middle">L’ORIGINAL</text>
    <text class="tagline" x="590" y="810" text-anchor="middle">ORIGINAL</text>
    <circle class="seal-ring" cx="395" cy="800" r="50"/>
    <circle class="seal" cx="395" cy="800" r="38"/>

    <g class="divider">
      <line class="rule" x1="85" y1="877" x2="705" y2="877"/>
      <ellipse class="knob" cx="82" cy="877" rx="8" ry="6"/>
      <ellipse class="knob" cx="708" cy="877" rx="8" ry="6"/>
      <circle class="knob" cx="395" cy="877" r="6"/>
    </g>

    <rect class="facts-band" x="78" y="906" width="634" height="69"/>
    <text class="facts" x="112" y="955">1L</text>
    <text class="facts" x="680" y="955" text-anchor="end">43% VOL</text>

    <g class="divider">
      <line class="rule" x1="85" y1="1003" x2="705" y2="1003"/>
      <ellipse class="knob" cx="82" cy="1003" rx="8" ry="6"/>
      <ellipse class="knob" cx="708" cy="1003" rx="8" ry="6"/>
      <circle class="knob" cx="395" cy="1003" r="6"/>
    </g>
  </svg>

</main>
</body>
</html>
```